Personal Development Business needs a Business Card Design Project

We need a buiness card design for a new Personal Development business based in S. NSW in Australia called "Willow Path Within. Our target market is to women who are looking to re-enter the workforce, or already be in the workforce at the middle management level. As a result of consultations their outcomes will be, but not exclusive to: increased confidence, increased self esteem and self awareness, work-life balance, time management, positive thinking.
Behind the scenes of coaching and mentoring will be a spiritual "bent".
Anticipate a beautiful candle as a possible background - showing success and shining - see attachment which came off Framevault. Colours - Unsure until I see something that "grabs my attention". Not esoteric fluffy design but something that suggests safe, professional, supportive of personal journey without being too corporate.
Look forward to what you come up with.
Some designers have been requesting various bits of information.
Personal information. See attachment.
Two-sided please.
Gold lines at all four edges.
Many thanks
Mira
Business

```html
<!DOCTYPE html>
<html lang="en">
<head>
<meta charset="utf-8">
<title>Willow Path Within – Business Card</title>
<link rel="stylesheet" href="https://fonts.googleapis.com/css2?family=Arimo:wght@400;700&display=swap">
<style>
  :root {
    --page: #ecebf0;
    --card-slate: #6a6995;
    --card-black: #050407;
    --ink-white: #ffffff;
    --ink-soft: #e6e5f2;
    --title-lilac: #e4c9f6;
    --band-deep: #2a1f63;
    --band-violet: #6b34b0;
    --band-magenta: #9a4fd0;
    --photo-teal: #1f7f8c;
    --photo-green: #1f5a34;
    --photo-violet: #4b2a7a;
    --edge-gold: #d4af37;
  }
  * { box-sizing: border-box; margin: 0; padding: 0; }
  html, body {
    width: 1200px; height: 740px; overflow: hidden;
    background: var(--page);
    font-family: "Arimo", Arial, sans-serif;
  }
  .canvas { position: relative; width: 1200px; height: 740px; }
  .card {
    position: absolute; top: 215px; width: 540px; height: 310px;
    overflow: hidden; border-radius: 2px;
    box-shadow: 0 10px 30px rgba(30, 20, 50, 0.25);
  }
  .card__edge {
    position: absolute; inset: 7px;
    border: 1.5px solid var(--edge-gold);
    pointer-events: none; z-index: 5;
  }

  /* ---------- Contact side ---------- */
  .card--contact { left: 40px; background: var(--card-slate); color: var(--ink-white); }
  .contact__name {
    position: absolute; left: 32px; top: 72px;
    font-size: 31px; font-weight: 700; letter-spacing: 0.2px;
  }
  .contact__credentials {
    position: absolute; left: 34px; top: 114px;
    font-size: 11.5px; line-height: 16px; color: var(--ink-soft);
    list-style: none;
  }
  .contact__divider {
    position: absolute; left: 262px; top: 34px; width: 1px; height: 130px;
    background: var(--ink-soft);
  }
  .contact__details { position: absolute; left: 282px; top: 44px; list-style: none; }
  .contact__row {
    display: flex; align-items: center; gap: 10px;
    height: 34px; font-size: 12px; color: var(--ink-soft);
  }
  .contact__row svg { width: 17px; height: 17px; flex: none; }
  .contact__band {
    position: absolute; left: 0; right: 0; top: 200px; bottom: 0;
    background: linear-gradient(100deg, var(--band-deep), var(--band-violet) 45%, var(--band-magenta) 70%, var(--band-deep));
  }
  .contact__outcomes {
    position: absolute; left: 32px; right: 24px; top: 222px;
    display: flex; justify-content: space-between; list-style: none;
    font-size: 15px; color: var(--ink-white);
  }
  .contact__outcomes li { display: flex; align-items: center; gap: 7px; }
  .contact__outcomes li::before {
    content: ""; width: 12px; height: 12px; border-radius: 50%;
    background: var(--ink-white); border: 1px solid #333;
  }

  /* ---------- Brand side ---------- */
  .card--brand { left: 620px; background: var(--card-black); }
  .brand__photo {
    position: absolute; inset: 0;
    background:
      linear-gradient(180deg, transparent 55%, var(--card-black) 100%),
      linear-gradient(120deg, var(--photo-green) 0%, var(--photo-teal) 40%, var(--photo-violet) 75%, var(--card-black) 100%);
  }
  .brand__name {
    position: absolute; right: 26px; bottom: 58px;
    font-size: 34px; font-weight: 700; color: var(--title-lilac);
  }
  .brand__tagline {
    position: absolute; right: 26px; bottom: 32px;
    font-size: 16px; font-weight: 700; color: var(--ink-white);
  }
</style>
</head>
<body>
<main class="canvas">

  <section class="card card--contact" aria-label="Contact side">
    <div class="contact__band" role="img" aria-label="Photograph of purple flowers"></div>
    <h1 class="contact__name">Mira Ashby</h1>
    <ul class="contact__credentials">
      <li>Grad Dip (Mgt) WCU</li>
      <li>BA American History (CNU)</li>
      <li>Master NLP</li>
    </ul>
    <div class="contact__divider"></div>
    <ul class="contact__details">
      <li class="contact__row">
        <svg viewBox="0 0 20 20" fill="none" stroke="#ffffff" stroke-width="1.3">
          <circle cx="10" cy="10" r="8"/><ellipse cx="10" cy="10" rx="3.5" ry="8"/>
          <line x1="2" y1="10" x2="18" y2="10"/><line x1="3.5" y1="6" x2="16.5" y2="6"/><line x1="3.5" y1="14" x2="16.5" y2="14"/>
        </svg>
        willowpathwithin.com.au
      </li>
      <li class="contact__row">
        <svg viewBox="0 0 20 20">
          <rect x="1" y="1" width="18" height="18" rx="3" fill="#ffffff"/>
          <path d="M7 5 l2 0 l1 3 l-1.5 1 q1 2.5 3.5 3.5 l1 -1.5 l3 1 l0 2 q-1 1.5 -3 1 q-6 -2 -7 -8 q0 -1.5 1 -2 z" fill="#6a6995"/>
        </svg>
        0400 555 182
      </li>
      <li class="contact__row">
        <svg viewBox="0 0 20 20" fill="#ffffff" stroke="#6a6995" stroke-width="1.2">
          <rect x="1.5" y="4" width="17" height="12"/><polyline points="1.5,4 10,11 18.5,4" fill="none"/>
        </svg>
        miraatwillow@tendrilmail.com.au
      </li>
    </ul>
    <ul class="contact__outcomes">
      <li>Self Awareness</li>
      <li>Confidence</li>
      <li>Work-Life Balance</li>
    </ul>
    <div class="card__edge"></div>
  </section>

  <section class="card card--brand" aria-label="Brand side">
    <div class="brand__photo" role="img" aria-label="Photograph of a lit candle among purple flowers and green leaves"></div>
    <h2 class="brand__name">Willow Path Within</h2>
    <p class="brand__tagline">Personal Development</p>
    <div class="card__edge"></div>
  </section>

</main>
</body>
</html>
```